New company website for Redfern Hollow Building Company

We're looking to build a new company website that customers can use to contact us, get quotes, view past projects (renovations, additions, new construction, etc.), & learn more about our business. We want to use WordPress for our website and have already purchased the Divi theme (by Quillmark Studio). Using that theme isn't required but we already have several examples of websites that we want to model our site after that use this theme. The "look" we're after is simple, light, & clean.

Target Market(s)

Residential remodeling, renovations, and new construction.

Industry/Entity Type

Residential Construction

Coding

Coded - Design and coding required

Number of Pages Required

5+ page

Font styles to use
Sans Serif

Colors
33a6d7
aaaaaa

Requirements
Must have
• We require the website to be coded using the Divi theme. We'll be upgrading the project to include this today or tomorrow.
• The navigation bar should be static & remain at the top of the page. When scrolling we'd like the logo & info in the nav bar to size down. Here's an example of a site that does this: https://tovamerihomes.example/
Nice to have
• In the gallery with pictures of our finished product/jobs, when you mouse over the image, we'd like there to be additional info that shows up. For example, look at this gallery: https://tovamerihomes.example/projectcategories/kitchens/ We'll add a name/location of the job like: "Garvey kitchen - Apex, N.C."
• If you go to this website: https://plinvorworks.example/ and scroll down to the pictures, we like how the picture moves and is interactive.

```html
<!DOCTYPE html>
<html lang="en">
<head>
<meta charset="utf-8">
<title>Redfern Hollow Building Company</title>
<link href="https://fonts.googleapis.com/css2?family=Comfortaa:wght@400;600;700&family=Montserrat:wght@400;600;700&display=swap" rel="stylesheet">
<style>
:root{
  --blue:#33a6d7;
  --grey:#aaaaaa;
  --ink:#2b2b2b;
  --stage:#efefef;
  --paper:#ffffff;
  --soft:#f8f9fa;
  --dark:#3a3a3a;
}
*{box-sizing:border-box;margin:0;padding:0}
html,body{width:1200px;height:1200px;overflow:hidden;background:var(--stage)}
.stage{position:absolute;left:0;top:0;width:1500px;height:1500px;transform:scale(.8);transform-origin:0 0}
.page{position:absolute;left:408px;top:0;width:685px;height:1500px;background:var(--paper);font-family:"Montserrat",sans-serif;color:var(--ink)}
.abs{position:absolute}
.display{font-family:"Comfortaa",sans-serif}
.blue{color:var(--blue)}
.logo{font-family:"Montserrat",sans-serif;font-weight:700;color:#444;font-size:9.5px;line-height:1;letter-spacing:.2px}
.logo small{display:block;font-size:5.5px;letter-spacing:2.6px;color:var(--blue);font-weight:600;margin-top:1px}
.info{font-size:5.5px;color:var(--blue);line-height:1.45;display:flex;gap:5px;align-items:flex-start}
.info svg{flex:none;margin-top:1px}
.btn-start{left:528px;top:7px;width:67px;height:18px;background:var(--blue);color:#fff;font-size:6.5px;display:flex;align-items:center;justify-content:center}
.nav{left:215px;top:38px;display:flex;gap:8px;font-size:5.2px;font-weight:600;color:#333;white-space:nowrap}
.nav .on{color:var(--blue)}
.dropdown{left:303px;top:46px;width:52px;height:33px;background:var(--blue);color:#fff;font-size:5.5px;font-weight:600;padding:5px 0 0 11px;line-height:2.3}
.photo{position:absolute}
.hero{left:0;top:54px;width:685px;height:247px;background:linear-gradient(100deg,#dcd9d2 0%,#eeeeec 35%,#c9cbcc 60%,#8f9396 100%)}
.hero-title{left:171px;top:141px;width:340px;height:71px;background:rgba(51,166,215,.85);color:#fff;font-size:24px;font-weight:700;text-align:center;line-height:26px;padding-top:8px}
.hero-btn{left:295px;top:208px;width:87px;height:19px;background:#fff;color:var(--blue);font-size:8px;display:flex;align-items:center;justify-content:center}
.history{left:0;top:301px;width:685px;height:279px;background:var(--soft)}
.tab{left:86px;top:363px;width:26px;height:177px;background:#4a4a4a;color:#fff;font-size:8.5px;font-weight:700;writing-mode:vertical-rl;transform:rotate(180deg);display:flex;align-items:center;justify-content:center}
.h2{font-size:17px}
.para{font-size:5.6px;line-height:1.75;color:#333}
.thumb-cap{font-size:6px;color:#444;text-align:center;width:85px}
.section-h{font-size:23px;line-height:24px}
.card-label{height:26px;width:152px;background:var(--blue);color:#fff;font-family:"Comfortaa",sans-serif;font-size:16px;display:flex;align-items:center;padding-left:24px;bottom:15px;left:0}
.avatar{width:87px;height:87px;border-radius:50%;top:1007px}
.quote-name{font-size:7px;text-align:center;width:110px;top:1100px}
.quote-text{font-size:5.5px;line-height:1.45;text-align:center;width:90px;top:1113px;color:#333}
.quote-band{left:0;top:1217px;width:685px;height:149px;background:var(--dark)}
.form{left:353px;top:1232px;width:245px;height:118px;background:var(--blue);color:#fff;font-size:5.5px;padding:10px 0 0 11px}
.form .field{height:21px;border-bottom:1px solid rgba(255,255,255,.45);margin-right:0;padding-top:0}
.send{left:360px;top:1332px;width:46px;height:16px;background:#fff;color:var(--blue);font-size:7px;font-weight:600;display:flex;align-items:center;justify-content:center}
.fnav{left:242px;top:1411px;display:flex;gap:9.5px;font-size:5.2px;font-weight:600;color:#333;white-space:nowrap}
.social{left:252px;top:1431px;display:flex;gap:10px}
.social span{width:8px;height:8px;border-radius:50%;border:1.3px solid #444}
</style>
</head>
<body>
<div class="stage">
<main class="page">

  <header>
    <div class="abs logo" style="left:88px;top:21px">REDFERN HOLLOW<small>BUILDING COMPANY</small></div>
    <div class="abs info" style="left:345px;top:8px">
      <svg width="8" height="11" viewBox="0 0 8 11"><path d="M4 0a4 4 0 0 1 4 4c0 3-4 7-4 7S0 7 0 4a4 4 0 0 1 4-4z" fill="#33a6d7"/><circle cx="4" cy="4" r="1.5" fill="#fff"/></svg>
      <span>48 Alder Row, Suite B<br>Millbrook, NC 27599</span>
    </div>
    <div class="abs" style="left:440px;top:6px;width:1px;height:20px;background:var(--grey)"></div>
    <div class="abs info" style="left:450px;top:8px">
      <svg width="8" height="8" viewBox="0 0 10 10"><path d="M2 0l2 2.5-1.2 1.3a6 6 0 0 0 3.4 3.4L7.5 6 10 8 8.5 10C4 10 0 6 0 1.5z" fill="#33a6d7"/></svg>
      <span>CALL US TODAY!<br>555.014.2290</span>
    </div>
    <div class="abs btn-start">Getting Started</div>
    <nav class="abs nav">
      <span>Our Proven Process ⌄</span><span>FAQs ⌄</span><span class="on">Who We Are ⌄</span><span>Specialties ⌄</span><span>Portfolio ⌄</span><span>Contact Us</span><span style="margin-left:6px">Client Portal ⌄</span><span>Start Planning Your Project</span>
    </nav>
  </header>

  <section>
    <div class="photo hero" role="img" aria-label="Photo of a bright remodeled kitchen with white cabinets, island and bar stools"></div>
    <div class="abs dropdown"><div>Our Story</div><div>Our Team</div></div>
    <h1 class="abs hero-title display">Your design and remodel<br>partner for life</h1>
    <div class="abs hero-btn">Contact Us Now</div>
  </section>

  <section>
    <div class="abs history"></div>
    <div class="abs tab">History of Expirence</div>
    <div class="photo" style="left:112px;top:357px;width:207px;height:188px;background:linear-gradient(160deg,#e9ebea,#c8c4bc 55%,#8a7b6a)" role="img" aria-label="Photo of a kitchen with pendant lights and granite island"></div>
    <h2 class="abs h2 display" style="left:329px;top:365px">History of <span class="blue">Experience</span></h2>
    <p class="abs para" style="left:330px;top:401px;width:265px">Aenean vulputate eleifend tellus. Aenean leo ligula, porttitor eu, consequat vitae, eleifend ac, enim. Aliquam lorem ante, dapibus in, viverra quis, feugiat a, tellus. Phasellus viverra nulla ut metus varius laoreet. Quisque rutrum.</p>
    <p class="abs para" style="left:330px;top:440px;width:265px">Aenean vulputate eleifend tellus. Aenean leo ligula, porttitor eu, consequat vitae, eleifend ac, enim. Aliquam lorem ante, dapibus in, viverra quis, feugiat a, tellus. Phasellus viverra nulla ut metus varius laoreet. Quisque rutrum.</p>
    <div class="abs blue" style="left:330px;top:481px;font-size:6px">READ MORE</div>
    <div class="photo" style="left:331px;top:498px;width:79px;height:49px;background:linear-gradient(135deg,#d8d4cc,#8c7a66)" role="img" aria-label="Photo of a finished kitchen"></div>
    <div class="photo" style="left:420px;top:498px;width:79px;height:49px;background:linear-gradient(135deg,#e2dfdb,#7a5b48)" role="img" aria-label="Photo of a kitchen with dark wood cabinets"></div>
    <div class="photo" style="left:507px;top:498px;width:79px;height:49px;background:linear-gradient(135deg,#9a9a9a,#5a5a5a)" role="img" aria-label="Photo of a kitchen interior"></div>
    <div class="abs thumb-cap" style="left:329px;top:550px">Proven Trust</div>
    <div class="abs thumb-cap" style="left:417px;top:550px">Constant Communication</div>
    <div class="abs thumb-cap" style="left:505px;top:550px">History of Experience</div>
  </section>

  <section>
    <h2 class="abs section-h display" style="left:85px;top:618px"><span class="blue">Transformations</span><br>within your reach</h2>
    <p class="abs para" style="left:313px;top:626px;width:290px;line-height:1.7">Aenean imperdiet. Etiam ultricies nisi vel augue. Curabitur ullamcorper ultricies nisi. Nam eget dui. Etiam rhoncus. Maecenas tempus, tellus eget condimentum rhoncus, sem quam semper libero.</p>
    <div class="photo" style="left:0;top:690px;width:223px;height:203px;background:linear-gradient(120deg,#eef0f0,#c9cccd 55%,#b5a894)" role="img" aria-label="Photo of a remodeled bathroom vanity"><div class="abs card-label">Bathroom</div></div>
    <div class="photo" style="left:231px;top:690px;width:223px;height:203px;background:linear-gradient(120deg,#cfc7b2,#e6dfcc 50%,#3f4a4d)" role="img" aria-label="Photo of a remodeled kitchen with cream cabinets"><div class="abs card-label">Kitchen</div></div>
    <div class="photo" style="left:462px;top:690px;width:223px;height:203px;background:linear-gradient(120deg,#f2f2f2,#6b4b3c 50%,#cfcac2)" role="img" aria-label="Photo of a new kitchen with dark cabinets and pendant lights"><div class="abs card-label">New Spaces</div></div>
  </section>

  <section>
    <h2 class="abs section-h display" style="left:0;width:685px;text-align:center;top:945px"><span class="blue">Client</span> Testimonial</h2>
    <div class="abs avatar" style="left:136px;background:linear-gradient(#5a9fc6,#a03030)" role="img" aria-label="Portrait of client Russel Odeku"></div>
    <div class="abs avatar" style="left:299px;background:linear-gradient(#6b4a3a,#b88560)" role="img" aria-label="Portrait of client Marisa Vell"></div>
    <div class="abs avatar" style="left:462px;background:linear-gradient(#c9d0d6,#7d8a84)" role="img" aria-label="Portrait of client Jonah Ferrow"></div>
    <div class="abs quote-name" style="left:124px">- Russel Odeku</div>
    <div class="abs quote-name" style="left:287px">- Marisa Vell</div>
    <div class="abs quote-name" style="left:450px">- Jonah Ferrow</div>
    <p class="abs quote-text" style="left:134px">Aenean imperdiet. Etiam ultricies nisi vel augue. Curabitur ullamcorper ultricies nisi. Nam eget dui. Etiam rhoncus. Maecenas tempus, tellus eget condimentum rhoncus, sem quam semper libero.</p>
    <p class="abs quote-text" style="left:297px">Aenean imperdiet. Etiam ultricies nisi vel augue. Curabitur ullamcorper ultricies nisi. Nam eget dui. Etiam rhoncus. Maecenas tempus, tellus eget condimentum rhoncus, sem quam semper libero.</p>
    <p class="abs quote-text" style="left:460px">Aenean imperdiet. Etiam ultricies nisi vel augue. Curabitur ullamcorper ultricies nisi. Nam eget dui. Etiam rhoncus. Maecenas tempus, tellus eget condimentum rhoncus, sem quam semper libero.</p>
  </section>

  <section>
    <div class="abs quote-band" role="img" aria-label="Dimmed photo of a bathroom interior"></div>
    <div class="photo" style="left:85px;top:1232px;width:268px;height:118px;background:linear-gradient(110deg,#3d3a36,#8f8676 55%,#6a6258)" role="img" aria-label="Photo of a freestanding bathtub"></div>
    <h2 class="abs display" style="left:182px;top:1278px;color:#fff;font-size:19px;font-weight:400">Request A Quote</h2>
    <form class="abs form">
      <div class="field">Name*</div>
      <div class="field">Email*</div>
      <div class="field">Phone*</div>
      <div class="field" style="border:none">Comment</div>
    </form>
    <div class="abs send">Send</div>
  </section>

  <footer>
    <div class="abs logo" style="left:88px;top:1406px">REDFERN HOLLOW<small>BUILDING COMPANY</small></div>
    <div class="abs info" style="left:88px;top:1432px">
      <svg width="8" height="8" viewBox="0 0 10 10"><path d="M2 0l2 2.5-1.2 1.3a6 6 0 0 0 3.4 3.4L7.5 6 10 8 8.5 10C4 10 0 6 0 1.5z" fill="#33a6d7"/></svg>
      <span>CALL US TODAY!<br>555.014.2290</span>
    </div>
    <div class="abs info" style="left:88px;top:1457px">
      <svg width="8" height="11" viewBox="0 0 8 11"><path d="M4 0a4 4 0 0 1 4 4c0 3-4 7-4 7S0 7 0 4a4 4 0 0 1 4-4z" fill="#33a6d7"/><circle cx="4" cy="4" r="1.5" fill="#fff"/></svg>
      <span>48 Alder Row, Suite B<br>Millbrook, NC 27599</span>
    </div>
    <nav class="abs fnav">
      <span>Our Proven Process</span><span>FAQs</span><span>Who We Are</span><span>Specialties</span><span>Portfolio</span><span>Contact Us</span><span>Client Portal</span><span>Start Planning Your Project</span>
    </nav>
    <div class="abs social"><span></span><span></span><span></span><span></span></div>
    <div class="abs" style="left:248px;top:1457px;font-size:5.5px;color:#333">©Redfern Hollow Building Company &nbsp;|&nbsp; 2018</div>
  </footer>

</main>
</div>
</body>
</html>
```